Falcon ridge RV Retreat business card

I need a design card for the logo I just had made on here. I will provide it and please make some cool designs, thank you.

I would like the card to have
- phone number (865-219-7652)
- email ( falconridgerv@examplemail.com)
- address to the park ( 5186 Copper Kettle Hollow rd, Maryville, TN) ZIP: 37946
on the back for double sided id like some lines for writing on. thanks

please follow the logo we provided in the files, I can provide the photoshop file if you need it.

please note this is in the Smokey mountains of Tennessee

Target Market(s)

cabin/rv rentals

Industry/Entity Type

rv/campground/cabin rentals

Contact Information for Business Card

address/email/phone number I added details in brief

Requirements
Must have
• on the back add a bear or something cool

```html
<!DOCTYPE html>
<html lang="en">
<head>
<meta charset="utf-8">
<title>Falcon ridge RV Retreat – Business Card</title>
<link href="https://fonts.googleapis.com/css2?family=EB+Garamond:wght@400;500&display=swap" rel="stylesheet">
<style>
  :root {
    --backdrop: #c2c2c2;
    --paper: #ffffff;
    --gold: #b58b3b;
    --art-light: #efe2c6;
    --art-deep: #d9bf88;
  }
  * { box-sizing: border-box; margin: 0; padding: 0; }
  html, body { width: 1200px; height: 848px; overflow: hidden; }
  body {
    background: var(--backdrop);
    font-family: "EB Garamond", Georgia, serif;
    position: relative;
  }
  .card {
    position: absolute;
    top: 149px;
    width: 320px;
    height: 550px;
    background: var(--paper);
    box-shadow: 0 6px 18px rgba(0,0,0,0.18);
  }
  .card--front { left: 250px; }
  .card--back { left: 630px; }
  .card__frame {
    position: absolute;
    inset: 18px;
    border: 1.2px solid var(--gold);
    border-radius: 18px;
  }
  .front__brand {
    position: absolute;
    top: 112px;
    left: 0; right: 0;
    text-align: center;
    color: var(--gold);
    font-weight: 500;
    font-size: 32px;
    line-height: 1.05;
  }
  .front__brand-mark {
    display: block;
    width: 104px; height: 104px;
    margin: 0 auto 16px;
    border-radius: 50%;
    border: 1.5px solid var(--gold);
  }
  .front__contact {
    position: absolute;
    top: 352px;
    left: 0; right: 0;
    text-align: center;
    color: var(--gold);
  }
  .contact__phone { font-size: 27px; font-weight: 500; line-height: 1.1; }
  .contact__email { font-size: 15px; margin-top: 4px; }
  .contact__address { font-size: 16.5px; line-height: 1.25; margin-top: 20px; }
  .back__art {
    position: absolute;
    top: 112px;
    left: 50%;
    width: 160px; height: 160px;
    margin-left: -80px;
    border-radius: 50%;
    border: 1.5px solid var(--gold);
    background: radial-gradient(circle at 50% 45%, var(--art-light), var(--art-deep));
  }
  .back__lines {
    position: absolute;
    top: 300px;
    left: 52px; right: 52px;
    list-style: none;
  }
  .back__lines li {
    height: 38px;
    border-bottom: 1px solid var(--gold);
  }
</style>
</head>
<body>
  <section class="card card--front">
    <div class="card__frame"></div>
    <div class="front__brand">
      <span class="front__brand-mark"></span>
      Falcon ridge<br>RV Retreat
    </div>
    <div class="front__contact">
      <p class="contact__phone">Tel. 865-219-7652</p>
      <p class="contact__email">falconridgerv@examplemail.com</p>
      <p class="contact__address">5186 Copper Kettle Hollow rd,<br>Maryville, TN 37946</p>
    </div>
  </section>

  <section class="card card--back">
    <div class="card__frame"></div>
    <div class="back__art" role="img" aria-label="Gold line illustration of a log cabin among pine trees and mountains under a rising sun, inside a circle"></div>
    <ul class="back__lines">
      <li></li><li></li><li></li><li></li><li></li>
    </ul>
  </section>
</body>
</html>
```